New shirt company looking for a fun and edgy online retail website design

We're a new company looking for a simple yet attractive website to sell shirts/tops to a mostly younger female audience. Our name is Tilvo Shirt Co. and the ArtPavilion logo is uploaded. We're thinking a home page, three separate pages for our shirt "collections", and a contact page/cart page for a grand total of 5 pages. We'd like the website to be coded, easy for the consumer to navigate/shop/checkout, and easy to link to various social media platforms and online websites. For colors, we're aiming for various blues, light grey, and maybe tan/khaki. Our goal is to launch with approximately 20-30 tops/shirts (or 7-10) per page. Please let us know if you have any questions and thank you for helping us! We are very excited to see what is created!

Target Market(s)

Female teens to early twenties

Coding

Coded - Design and coding required

Number of Pages Required

3 page

Font styles to use
Decorative
Script

Colors
cee9f5
85cae6
33a6d7
0393ce
cfdfed
85acd3

Requirements
Must have
• Online shopping/purchasing capabilities, dropdowns to select sizes for each item, easy to add/remove new or seasoned items.

```html
<!DOCTYPE html>
<html lang="en">
<head>
<meta charset="utf-8">
<title>Tilvo Shirt Co. – Product</title>
<link href="https://fonts.googleapis.com/css2?family=Alfa+Slab+One&family=Arimo:wght@400;700&family=Montserrat:wght@500;600;700&display=swap" rel="stylesheet">
<style>
:root{
  --navy:#0d4f9c;
  --blue:#1a8fd0;
  --sky:#33a6d7;
  --bright:#0393ce;
  --pale:#f0f6fb;
  --ice:#cee9f5;
  --line:#dde6ee;
  --text:#555c63;
  --muted:#7d848b;
  --ink:#111;
  --white:#fff;
  --star:#f5a623;
}
*{margin:0;padding:0;box-sizing:border-box}
html,body{width:671px;height:1200px;overflow:hidden;background:var(--white)}
body{font-family:"Arimo",Arial,sans-serif;color:var(--text)}
.page{position:relative;width:671px;height:1200px;overflow:hidden}
.abs{position:absolute}

/* header */
.site-header{left:0;top:0;width:671px;height:59px;background:var(--pale)}
.brand{font-family:"Montserrat",sans-serif;font-weight:700;color:var(--navy);font-size:8.5px;letter-spacing:.3px;white-space:nowrap}
.header-brand{left:90px;top:24px}
.main-nav a{position:absolute;top:25px;font-size:6.5px;color:var(--muted);text-decoration:none;white-space:nowrap}
.main-nav a.active{color:var(--blue)}
.account{top:25px;font-size:6.5px;color:#444;white-space:nowrap}

/* product */
.thumb{left:90px;width:31px;height:38px;border:1px solid #eef1f4;background:linear-gradient(180deg,#e9eef3,#c9dbea 55%,#a3694a 100%)}
.hero-frame{left:128px;top:101px;width:187px;height:225px;border:1px solid #eef1f4;background:var(--white)}
.hero-photo{left:40px;top:48px;width:100px;height:160px;border-radius:40px 40px 12px 12px;background:linear-gradient(180deg,#e4eef7 0%,#a9c8e3 45%,#8e5a3a 85%,#f4f8fb 100%)}
.meta{left:336px;font-size:6px;color:#555}
.product-title{left:336px;top:130px;width:290px;font-family:"Alfa Slab One",serif;font-size:21px;line-height:21px;color:var(--navy);letter-spacing:.4px}
.price{left:336px;top:178px;font-family:"Montserrat",sans-serif;font-weight:600;font-size:8.5px;color:var(--blue)}
.rating{left:335px;top:193px;display:flex;align-items:center;gap:2px;font-size:5.3px;color:var(--muted)}
.rating span{margin-left:5px}
.summary{left:336px;top:217px;width:245px;font-size:6px;line-height:11.7px;color:var(--muted)}
.qty{left:338px;top:265px;width:55px;height:17px;border:1px solid #333;display:flex;font-size:6px;color:#222}
.qty div{display:flex;align-items:center;justify-content:center}
.qty .step{width:16px}
.qty .num{flex:1;border-left:1px solid #333;border-right:1px solid #333;font-weight:700}
.cart-btn{left:401px;top:265px;width:63px;height:17px;background:var(--navy);color:var(--white);font-family:"Montserrat",sans-serif;font-size:6px;display:flex;align-items:center;justify-content:center}
.social{width:19px;height:19px;border-radius:50%;border:1px solid var(--blue)}
.social.solid{background:var(--navy);border-color:var(--navy)}

/* tabs */
.tab{top:385px;font-family:"Montserrat",sans-serif;font-weight:600;font-size:8.5px}
.tab.active{color:var(--blue)}
.tab.other{color:var(--navy)}
.tab-rule{left:90px;top:405px;width:491px;height:1px;background:var(--line)}
.tab-mark{left:90px;top:404px;width:67px;height:1.5px;background:var(--blue)}
.spec-label{left:91px;font-size:6px;color:var(--muted)}
.spec-text{left:187px;width:275px;font-size:6px;line-height:11.7px;color:var(--muted)}

/* newsletter */
.newsletter{left:0;top:580px;width:671px;height:226px;background:linear-gradient(90deg,#1561ae 0%,#1877c1 55%,#1b9ad6 100%)}
.news-title{left:91px;top:629px;font-family:"Alfa Slab One",serif;font-size:20px;color:var(--white);letter-spacing:.5px}
.news-text{left:91px;top:664px;width:300px;font-size:6.3px;line-height:11.7px;color:var(--white)}
.email{left:90px;top:699px;width:273px;height:25px;background:var(--white);border-radius:1px;font-size:6.3px;color:#555;padding:9px 0 0 9px}
.subscribe{left:90px;top:733px;width:75px;height:25px;background:var(--sky);border-radius:2px;color:var(--white);font-size:7px;display:flex;align-items:center;justify-content:center}
.model{left:387px;top:580px;width:184px;height:226px}

/* gallery */
.hashtag{left:0;top:836px;width:671px;text-align:center;font-family:"Alfa Slab One",serif;font-size:20px;color:var(--ink);letter-spacing:.5px}
.shot{top:882px;width:92px;height:92px}

/* footer */
.site-footer{left:0;top:1007px;width:671px;height:193px;background:var(--pale)}
.footer-brand{left:0;top:1053px;width:671px;text-align:center}
.footer-nav{left:0;top:1091px;width:671px;text-align:center;font-size:6.5px;color:var(--muted);white-space:nowrap}
.footer-nav span{margin:0 6px}
.foot-social{top:1112px;width:17px;height:17px;border-radius:50%}
.footer-rule{left:0;top:1162px;width:671px;height:1px;background:#dbe9f3}
.copyright{left:0;top:1177px;width:671px;text-align:center;font-size:5.2px;color:#6cc3ea}
</style>
</head>
<body>
<div class="page">

  <header class="site-header abs"></header>
  <div class="brand header-brand abs">Tilvo Shirt Co.</div>
  <nav class="main-nav">
    <a class="active" style="left:190px">Home</a>
    <a style="left:221px">Collections</a>
    <a style="left:267px">Shop</a>
    <a style="left:295px">Contact Us</a>
  </nav>
  <svg class="abs" style="left:340px;top:19px" width="20" height="20" viewBox="0 0 20 20" aria-label="Search">
    <circle cx="10" cy="10" r="9.2" fill="none" stroke="#0d4f9c" stroke-width=".8"/>
    <circle cx="9.3" cy="9.3" r="3" fill="none" stroke="#0d4f9c" stroke-width=".8"/>
    <line x1="11.5" y1="11.5" x2="13.5" y2="13.5" stroke="#0d4f9c" stroke-width=".8"/>
  </svg>
  <div class="account abs" style="left:471px">Sign Up &nbsp;|&nbsp; Login</div>
  <div class="account abs" style="left:531px">My Cart</div>
  <svg class="abs" style="left:561px;top:18px" width="22" height="18" viewBox="0 0 22 18" aria-label="Cart">
    <path d="M1 5h2.5l2 7h7.5l2-5.5H4.5" fill="none" stroke="#1a8fd0" stroke-width="1.6" stroke-linejoin="round"/>
    <path d="M5 7h9.5l-1.6 4.3H6.2z" fill="#1a8fd0"/>
    <circle cx="6.5" cy="14.5" r="1.3" fill="#1a8fd0"/>
    <circle cx="12" cy="14.5" r="1.3" fill="#1a8fd0"/>
    <circle cx="15" cy="7" r="5" fill="#fff" stroke="#1a8fd0" stroke-width=".6"/>
    <text x="15" y="9" font-size="6" text-anchor="middle" fill="#111" font-family="Arimo,sans-serif">0</text>
  </svg>

  <!-- product gallery -->
  <div class="thumb abs" style="top:101px" role="img" aria-label="Product view thumbnail"></div>
  <div class="thumb abs" style="top:143px" role="img" aria-label="Product view thumbnail"></div>
  <div class="thumb abs" style="top:184px" role="img" aria-label="Product view thumbnail"></div>
  <div class="thumb abs" style="top:226px" role="img" aria-label="Product view thumbnail"></div>
  <div class="thumb abs" style="top:267px" role="img" aria-label="Product view thumbnail"></div>
  <div class="hero-frame abs">
    <div class="hero-photo abs" role="img" aria-label="Model wearing a light denim shirt and brown shorts"></div>
    <svg class="abs" style="left:145px;top:28px" width="14" height="14" viewBox="0 0 14 14" aria-label="Zoom">
      <line x1="7" y1="0" x2="7" y2="14" stroke="#222" stroke-width=".7"/>
      <line x1="0" y1="7" x2="14" y2="7" stroke="#222" stroke-width=".7"/>
    </svg>
  </div>

  <div class="meta abs" style="top:101px">Product Code: 001</div>
  <div class="meta abs" style="top:113px">Availablity: 40 Stock</div>
  <h1 class="product-title abs">LOREM IPSUM IS SIMPLE DUMMY TEXT</h1>
  <div class="price abs">$250.00</div>
  <div class="rating abs">
    <svg width="42" height="7" viewBox="0 0 42 7" aria-label="4 of 5 stars">
      <g fill="#f5a623">
        <path d="M3.5 0l1 2.3 2.5.2-1.9 1.6.6 2.5-2.2-1.3-2.2 1.3.6-2.5L0 2.5l2.5-.2z"/>
        <path transform="translate(8.5)" d="M3.5 0l1 2.3 2.5.2-1.9 1.6.6 2.5-2.2-1.3-2.2 1.3.6-2.5L0 2.5l2.5-.2z"/>
        <path transform="translate(17)" d="M3.5 0l1 2.3 2.5.2-1.9 1.6.6 2.5-2.2-1.3-2.2 1.3.6-2.5L0 2.5l2.5-.2z"/>
        <path transform="translate(25.5)" d="M3.5 0l1 2.3 2.5.2-1.9 1.6.6 2.5-2.2-1.3-2.2 1.3.6-2.5L0 2.5l2.5-.2z"/>
      </g>
      <path fill="#666" transform="translate(34)" d="M3.5 0l1 2.3 2.5.2-1.9 1.6.6 2.5-2.2-1.3-2.2 1.3.6-2.5L0 2.5l2.5-.2z"/>
    </svg>
    <span>(25 REVIEWS)</span>
  </div>
  <p class="summary abs">Lorem Ipsum is simply dummy text of the printing and typesetting industry. Lorem Ipsum has been the industry's standard dummy text ever since the 1500s, when an unknown printer took a galley of type and scrambled it to make a type specimen book.</p>
  <div class="qty abs"><div class="step">-</div><div class="num">10</div><div class="step">+</div></div>
  <div class="cart-btn abs">ADD TO CART</div>
  <div class="social solid abs" style="left:338px;top:296px" role="img" aria-label="Social link"></div>
  <div class="social abs" style="left:363px;top:296px" role="img" aria-label="Social link"></div>
  <div class="social abs" style="left:388px;top:296px" role="img" aria-label="Social link"></div>

  <!-- tabs -->
  <div class="tab active abs" style="left:91px">DISCRIPTION</div>
  <div class="tab other abs" style="left:171px">REVIEWS</div>
  <div class="tab-rule abs"></div>
  <div class="tab-mark abs"></div>

  <div class="spec-label abs" style="top:439px">Lorem Ipsum</div>
  <p class="spec-text abs" style="top:436px">Lorem Ipsum is simply dummy text of the printing and typesetting industry.</p>
  <div class="spec-label abs" style="top:460px">Lorem Ipsum</div>
  <p class="spec-text abs" style="top:457px">Lorem Ipsum is simply dummy text of the printing and typesetting industry. Lorem Ipsum has been the industry's standard dummy text ever since the 1500s.</p>
  <div class="spec-label abs" style="top:494px">Lorem Ipsum</div>
  <p class="spec-text abs" style="top:491px">Lorem Ipsum is simply dummy text of the printing and typesetting industry. Lorem Ipsum has been the industry's standard dummy text ever since the 1500s, when an unknown printer took a galley of type and scrambled it to make a type specimen book.</p>

  <!-- newsletter -->
  <section class="newsletter abs"></section>
  <h2 class="news-title abs">STAY UPDATED</h2>
  <p class="news-text abs">Lorem ipsum dolor sit amet, consectetur adipiscing elit, sed do eiusmod tempor incididunt ut labore et dolore magna aliqua.</p>
  <div class="email abs">Enter Email</div>
  <div class="subscribe abs">SUBCRIBE NOW</div>
  <svg class="model abs" viewBox="0 0 184 226" role="img" aria-label="Model with long orange hair in a striped shirt">
    <path d="M40 60 C60 40 110 30 150 45 L178 78 C186 90 184 110 176 130 L150 195 C140 215 120 226 100 226 L60 226 C40 210 20 170 10 130 C6 100 20 80 40 60z" fill="#cbe5f3"/>
    <path d="M30 75 C12 100 0 140 8 165 L55 220" fill="none" stroke="#e8f4fb" stroke-width="1"/>
    <path d="M70 226 L72 120 C76 70 90 20 110 0 L135 0 C150 30 150 80 148 130 L150 226z" fill="url(#modelTone)"/>
    <defs>
      <linearGradient id="modelTone" x1="0" y1="0" x2="0" y2="1">
        <stop offset="0" stop-color="#ef8a57"/>
        <stop offset=".45" stop-color="#cfe0ee"/>
        <stop offset=".85" stop-color="#a8c8e2"/>
        <stop offset="1" stop-color="#e9a6ad"/>
      </linearGradient>
    </defs>
  </svg>

  <!-- gallery -->
  <h2 class="hashtag abs">#TILVO SHIRT</h2>
  <div class="shot abs" style="left:93px;background:linear-gradient(180deg,#dfe3e7,#c9cdd2 50%,#3a3a3a)" role="img" aria-label="Model in a white tee by a railing"></div>
  <div class="shot abs" style="left:191px;background:linear-gradient(180deg,#9aa0a6,#c9d3dd 50%,#2b2f36)" role="img" aria-label="Model in a denim jacket on a street"></div>
  <div class="shot abs" style="left:289px;background:linear-gradient(135deg,#4d6a3a,#b46a44 45%,#5f86ad)" role="img" aria-label="Model in a denim jacket among leaves"></div>
  <div class="shot abs" style="left:388px;background:linear-gradient(90deg,#3a3733,#8c8885 45%,#c4a07a)" role="img" aria-label="Model in a grey jumpsuit by a stone wall"></div>
  <div class="shot abs" style="left:486px;background:linear-gradient(180deg,#5a4a2e,#d7d9e3 55%,#3f5f8c)" role="img" aria-label="Model in a white blouse and jeans"></div>

  <!-- footer -->
  <footer class="site-footer abs"></footer>
  <div class="brand footer-brand abs">Tilvo Shirt Co.</div>
  <nav class="footer-nav abs">Home<span>|</span>Collections<span>|</span>Shop<span>|</span>Checkout<span>|</span>Contact Us</nav>
  <div class="foot-social abs" style="left:308px;background:#4b6cb7" role="img" aria-label="Social link"></div>
  <div class="foot-social abs" style="left:327px;background:#2aa3e6" role="img" aria-label="Social link"></div>
  <div class="foot-social abs" style="left:346px;background:#c74a8a" role="img" aria-label="Social link"></div>
  <div class="footer-rule abs"></div>
  <div class="copyright abs">Copyright @ TILVO SHIRT COMPANY - 2020 . All Right Reserved.</div>

</div>
</body>
</html>
```